Refer a Friend A5 Flyer for Healthcare Staff

We need an A5 flyer that we can hand out to existing and new staff members promoting our Refer a friend Scheme. We need the leaflet to encourage staff to talk to their family and friends about joining our Healthcare Agency, which provides staff to local care related establishments. Using our logo and brand colours blue and green, as per our website, the final design will need to clearly convey the benefits and attractions of referring additional staff to the team. In addition is the promotion of our Circlebook page, requesting staff to like the page and to like and share various posts.

Target Market(s)

Healthcare and potential Healthcare Staff

Industry/Entity Type

Healthcare

Colors
33b8a4
3277b5

Requirements
Must have
• Company Logo, Brand colours,
• text; "Refer a Friend and receive a £50 Bonus after just 1 completed shift"
• text; "3 easy steps to refer a friend, 1 Fill out your name on the back of your Business Card 2 Hand the card to your friend or any person you wish to refer, 3 ask your friend to present the card to us when they attend their interview"
• text; "Like and share any of our Open Days on Circlebook for a chance to win a prize, you can find us easily by searching @CarewellPlacementGroup"
• text; "Like our Page to stay up to date with our events and offers"
Nice to have
• care worker / elderly care / support worker pictures
• Content / pics from website www.carewellplacementgroup.co.uk

```html
<!DOCTYPE html>
<html lang="en">
<head>
<meta charset="utf-8">
<title>Carewell Placement Group – Refer a Friend</title>
<link rel="stylesheet" href="https://fonts.googleapis.com/css2?family=Barlow+Semi+Condensed:wght@400;500;600;700&display=swap">
<style>
  :root {
    --teal: #33b8a4;
    --blue: #3277b5;
    --blue-deep: #2f6fae;
    --white: #ffffff;
    --text-teal: #2aa893;
  }
  * { box-sizing: border-box; margin: 0; padding: 0; }
  html, body {
    width: 886px;
    height: 1200px;
    overflow: hidden;
    background: var(--white);
  }
  .flyer {
    position: relative;
    width: 886px;
    height: 1200px;
    font-family: "Barlow Semi Condensed", "Arial Narrow", sans-serif;
    color: var(--white);
  }
  .flyer__shapes {
    position: absolute;
    inset: 0;
  }
  .brand {
    position: absolute;
    left: 74px;
    top: 78px;
    display: flex;
    align-items: center;
    gap: 14px;
  }
  .brand__dot {
    width: 30px;
    height: 30px;
    border-radius: 50%;
    background: var(--teal);
  }
  .brand__name {
    font-size: 38px;
    font-weight: 500;
    line-height: 1.05;
    color: var(--blue);
  }
  .steps__title {
    position: absolute;
    left: 446px;
    top: 230px;
    color: var(--blue);
    font-weight: 600;
    font-size: 28px;
    line-height: 1.15;
  }
  .steps__title span { display: block; }
  .steps__title span + span { padding-left: 8px; }
  .step {
    position: absolute;
    display: flex;
    align-items: center;
    gap: 12px;
  }
  .step__num {
    flex: none;
    width: 50px;
    height: 50px;
    border-radius: 50%;
    border: 3px solid var(--teal);
    background: var(--white);
    color: var(--blue);
    font-weight: 700;
    font-size: 36px;
    line-height: 44px;
    text-align: center;
  }
  .step__text {
    color: var(--text-teal);
    font-size: 17px;
    font-weight: 500;
    line-height: 1.35;
  }
  .step--one { left: 424px; top: 331px; }
  .step--one .step__text { margin-top: -22px; }
  .step--two { left: 468px; top: 434px; }
  .step--three { left: 512px; top: 532px; }
  .offer {
    position: absolute;
    left: 60px;
    top: 684px;
    width: 540px;
    text-align: center;
    font-weight: 600;
    line-height: 1.1;
  }
  .offer__lead { font-size: 35px; }
  .offer__amount { font-size: 48px; font-weight: 700; }
  .offer__tail { font-size: 35px; }
  .megaphone {
    position: absolute;
    left: 262px;
    top: 896px;
    width: 160px;
    height: 136px;
  }
  .social-prize {
    position: absolute;
    left: 470px;
    top: 880px;
    width: 346px;
    text-align: center;
    font-size: 20px;
    font-weight: 500;
    line-height: 1.45;
  }
  .social-prize strong { font-weight: 700; }
  .social-prize__win {
    font-size: 31px;
    font-weight: 700;
    line-height: 1.1;
  }
  .social-prize__handle { font-weight: 700; }
  .page-note {
    position: absolute;
    left: 40px;
    top: 1102px;
    font-size: 28px;
    font-weight: 500;
    line-height: 1.3;
  }
</style>
</head>
<body>
<main class="flyer">
  <svg class="flyer__shapes" width="886" height="1200" viewBox="0 0 886 1200" aria-hidden="false">
    <defs>
      <linearGradient id="carerGardenTone" x1="0" y1="0" x2="1" y2="1">
        <stop offset="0" stop-color="#8fae6a"/>
        <stop offset="0.5" stop-color="#c9a58c"/>
        <stop offset="1" stop-color="#8a9a86"/>
      </linearGradient>
      <linearGradient id="teamTone" x1="0" y1="0" x2="1" y2="1">
        <stop offset="0" stop-color="#f4f6f8"/>
        <stop offset="0.5" stop-color="#d8e3ef"/>
        <stop offset="1" stop-color="#f2f4f6"/>
      </linearGradient>
      <linearGradient id="carerChairTone" x1="0" y1="0" x2="1" y2="1">
        <stop offset="0" stop-color="#3e6fa3"/>
        <stop offset="0.55" stop-color="#d9c2b3"/>
        <stop offset="1" stop-color="#4fae8f"/>
      </linearGradient>
    </defs>
    <rect class="frame" x="0" y="0" width="886" height="1200" fill="var(--teal)"/>
    <rect class="panel-right" x="560" y="21" width="305" height="817" fill="var(--blue)"/>
    <rect class="band-bottom" x="20" y="838" width="845" height="342" fill="var(--blue)"/>
    <polygon class="band-bottom__stripe" points="20,890 830,1180 20,988" fill="var(--teal)"/>
    <polygon class="panel-white" points="20,21 586,21 865,620 865,678 624,678 700,838 411,228 20,228" fill="var(--white)"/>
    <polygon class="photo photo--carer-garden" role="img" aria-label="Photo of a smiling care worker with an elderly woman in a wheelchair outdoors" points="586,21 865,21 865,437 787,437" fill="url(#carerGardenTone)"/>
    <polygon class="photo photo--team" role="img" aria-label="Photo of a group of nurses in white uniforms joining hands in a team huddle" points="20,245 377,245 586,676 20,676" fill="url(#teamTone)"/>
    <polygon class="photo photo--carer-chair" role="img" aria-label="Photo of a care worker holding hands with a smiling elderly woman" points="624,678 865,678 865,838 700,838" fill="url(#carerChairTone)"/>
  </svg>

  <div class="brand">
    <span class="brand__dot"></span>
    <span class="brand__name">Carewell<br>Placement Group</span>
  </div>

  <h2 class="steps__title"><span>3 Easy steps</span><span>to refer a friend</span></h2>

  <div class="step step--one">
    <span class="step__num">1</span>
    <p class="step__text">Fill out your name<br>on the back of your<br>Business Card</p>
  </div>
  <div class="step step--two">
    <span class="step__num">2</span>
    <p class="step__text">Hand the card to your friend<br>or any person you wish to refer</p>
  </div>
  <div class="step step--three">
    <span class="step__num">3</span>
    <p class="step__text">Ask your friend to present<br>the card to us when they<br>attend their interview</p>
  </div>

  <div class="offer">
    <p class="offer__lead">Refer a Friend and receive a</p>
    <p class="offer__amount">£50 Bonus</p>
    <p class="offer__tail">after just 1 completed shift</p>
  </div>

  <svg class="megaphone" viewBox="0 0 160 136" aria-hidden="true">
    <g fill="var(--white)">
      <path d="M8 70 L20 104 L44 95 L32 61 Z"/>
      <path d="M36 58 L48 93 L104 90 L78 20 Z"/>
      <path d="M44 96 L58 94 L72 128 L60 132 Z"/>
    </g>
    <g fill="none" stroke="var(--white)" stroke-width="7" stroke-linecap="round">
      <path d="M104 36 Q116 48 112 64"/>
      <path d="M116 22 Q136 44 128 72"/>
      <path d="M128 8 Q156 40 144 80"/>
    </g>
  </svg>

  <div class="social-prize">
    <p><strong>Like and share</strong></p>
    <p>any of our Open Days on Circlebook</p>
    <p>for a chance to <span class="social-prize__win">win a prize</span></p>
    <p>you can find us easily by searching</p>
    <p class="social-prize__handle">@CarewellPlacementGroup</p>
  </div>

  <p class="page-note">Like our Page to stay up to date<br>with our events and offers</p>
</main>
</body>
</html>
```